Multilingual Website for a Medico Company

We need a multilingual Website for our Medico company that sells gloves and masks, the website should have 3-5 subpages on 5 different languages.

Industry/Entity Type

Medtech

Number of Pages Required

5+ page

Requirements
Must have
• Unique Design - No template
Should not have
• No Templates

```html
<!DOCTYPE html>
<html lang="en">
<head>
<meta charset="utf-8">
<title>Curamed – Shop</title>
<link href="https://fonts.googleapis.com/css2?family=Lato:wght@300;400;700;900&display=swap" rel="stylesheet">
<style>
  :root{
    --header-bg:#16280f;
    --footer-bg:#1a2f12;
    --footer-bar:#132209;
    --brand:#6cc12b;
    --button:#3d6a1f;
    --card-bg:#f3f0ea;
    --image-bg:#ffffff;
    --text:#2b2b2b;
    --muted:#7a7a7a;
    --white:#ffffff;
  }
  *{box-sizing:border-box;margin:0;padding:0}
  html,body{width:1200px;height:2182px;overflow:hidden}
  body{font-family:'Lato',sans-serif;color:var(--text);background:#fff;position:relative}

  .site-header{position:absolute;left:0;top:0;width:1200px;height:68px;background:var(--header-bg)}
  .logo{position:absolute;font-family:'Lato',sans-serif;font-weight:900;font-size:32px;color:var(--brand);letter-spacing:-.5px;display:flex;align-items:center;gap:8px}
  .logo-dot{width:14px;height:14px;border-radius:50%;background:var(--brand)}
  .site-header .logo{left:150px;top:14px}
  .main-nav{position:absolute;left:458px;top:22px;display:flex;gap:31px}
  .main-nav a{color:var(--white);text-decoration:none;font-weight:700;font-size:17px}
  .header-tools{position:absolute;left:878px;top:24px;display:flex;align-items:center;gap:20px}
  .cart{position:relative}
  .cart-count{position:absolute;right:-6px;top:-8px;width:16px;height:16px;border-radius:50%;background:var(--brand);color:var(--header-bg);font-size:10px;font-weight:900;display:flex;align-items:center;justify-content:center}

  .breadcrumb{position:absolute;left:150px;top:86px;font-size:15px;color:#555}
  .results-count{position:absolute;left:150px;top:147px;font-size:19px;color:#444}
  .sort-select{position:absolute;left:822px;top:136px;width:228px;height:47px;border:2px solid var(--button);border-radius:3px;display:flex;align-items:center;justify-content:space-between;padding:0 16px;font-size:14px;font-weight:700;color:#333}

  .product-grid{position:absolute;left:150px;top:222px;width:900px;display:grid;grid-template-columns:repeat(3,292px);column-gap:12px;row-gap:14px}
  .product-card{height:398px;background:var(--card-bg);box-shadow:0 1px 4px rgba(0,0,0,.12);position:relative}
  .product-image{height:188px;background:var(--image-bg);display:flex;align-items:center;justify-content:center}
  .product-image span{display:block;width:180px;height:130px;border-radius:6px}
  .tone-blue span{background:linear-gradient(135deg,#dfeefa,#3d7fc0)}
  .tone-sky span{background:linear-gradient(135deg,#e4f3fb,#5aa9d8)}
  .tone-dark span{background:linear-gradient(135deg,#eef0f2,#1b1b1b)}
  .tone-white span{background:linear-gradient(135deg,#f5f5f5,#8a99a6)}
  .tone-teal span{width:120px;height:160px;background:linear-gradient(135deg,#bfe8ea,#2e9fab)}
  .tone-navy span{background:linear-gradient(135deg,#f3f4f7,#1f3f6e)}
  .product-head{display:flex;justify-content:space-between;align-items:baseline;padding:18px 15px 0 15px}
  .product-name{font-size:22px;font-weight:700;color:#333}
  .product-price{font-size:19px;font-weight:400;color:#333}
  .product-desc{padding:6px 16px 0 16px;font-size:13px;font-weight:300;line-height:20.3px;color:var(--muted)}
  .add-to-cart{position:absolute;left:71px;top:337px;width:150px;height:45px;background:var(--button);color:var(--white);font-weight:700;font-size:12.5px;display:flex;align-items:center;justify-content:center;border-radius:2px}

  .site-footer{position:absolute;left:0;top:1924px;width:1200px;height:258px;background:var(--footer-bg);color:var(--white)}
  .site-footer .logo{left:154px;top:14px}
  .footer-about{position:absolute;left:154px;top:70px;width:260px;font-size:13.5px;line-height:20.3px}
  .footer-heading{position:absolute;top:34px;font-size:17px;font-weight:700}
  .footer-links{position:absolute;top:69px;list-style:none;font-size:13.5px}
  .footer-links li{height:27px}
  .contact-item{position:absolute;left:885px;display:flex;gap:17px;font-size:13.5px;line-height:20px}
  .contact-item svg{flex:none;margin-top:1px}
  .footer-bar{position:absolute;left:0;bottom:0;width:1200px;height:35px;background:var(--footer-bar);display:flex;align-items:center;justify-content:center;font-size:13.5px}
</style>
</head>
<body>

<header class="site-header">
  <div class="logo"><span class="logo-dot"></span>curamed</div>
  <nav class="main-nav"><a href="#">Home</a><a href="#">Shop</a><a href="#">About</a><a href="#">Contact</a></nav>
  <div class="header-tools">
    <svg width="24" height="16" viewBox="0 0 24 16" aria-label="English"><rect width="24" height="16" fill="#1f3f8f"/><path d="M0 0L24 16M24 0L0 16" stroke="#fff" stroke-width="3"/><path d="M0 0L24 16M24 0L0 16" stroke="#c8102e" stroke-width="1"/><path d="M12 0V16M0 8H24" stroke="#fff" stroke-width="5"/><path d="M12 0V16M0 8H24" stroke="#c8102e" stroke-width="3"/></svg>
    <svg width="26" height="26" viewBox="0 0 26 26" fill="none" stroke="#fff" stroke-width="1.6"><circle cx="11" cy="11" r="9"/><path d="M17.5 17.5L25 25"/></svg>
    <svg width="26" height="28" viewBox="0 0 26 28" fill="none" stroke="#fff" stroke-width="1.6"><circle cx="13" cy="9" r="7"/><path d="M1 27c1-7 6-10 12-10s11 3 12 10"/></svg>
    <div class="cart">
      <svg width="26" height="26" viewBox="0 0 26 26" fill="none" stroke="#fff" stroke-width="1.6"><path d="M1 3h4l3 14h14l3-10H7"/><circle cx="10" cy="22" r="2"/><circle cx="20" cy="22" r="2"/></svg>
      <span class="cart-count">0</span>
    </div>
  </div>
</header>

<div class="breadcrumb">Home / Shop</div>
<div class="results-count">Showing all 12 results</div>
<div class="sort-select">Sort by price: high to low
  <svg width="14" height="8" viewBox="0 0 14 8" fill="none" stroke="#333" stroke-width="1.4"><path d="M1 1l6 6 6-6"/></svg>
</div>

<main class="product-grid">
  <article class="product-card"><div class="product-image tone-blue" role="img" aria-label="Box of 3-ply disposable face masks"><span></span></div><div class="product-head"><h3 class="product-name">Disposable Mask</h3><span class="product-price">$16.00</span></div><p class="product-desc">Lorem ipsum dolor sit amet, consectetur elit. Morbi pellentesque, nisi ac tincidunt varius, erat nulla tempor est, ac malesuada ex quam sit amet ipsum.</p><div class="add-to-cart">Add to cart</div></article>
  <article class="product-card"><div class="product-image tone-sky" role="img" aria-label="Box of surgical earloop masks"><span></span></div><div class="product-head"><h3 class="product-name">Surgical Mask</h3><span class="product-price">$22.00</span></div><p class="product-desc">Lorem ipsum dolor sit amet, consectetur elit. Morbi pellentesque, nisi ac tincidunt varius, erat nulla tempor est, ac malesuada ex quam sit amet ipsum.</p><div class="add-to-cart">Add to cart</div></article>
  <article class="product-card"><div class="product-image tone-dark" role="img" aria-label="Black reusable mask with its box"><span></span></div><div class="product-head"><h3 class="product-name">Reusable Mask</h3><span class="product-price">$26.00</span></div><p class="product-desc">Lorem ipsum dolor sit amet, consectetur elit. Morbi pellentesque, nisi ac tincidunt varius, erat nulla tempor est, ac malesuada ex quam sit amet ipsum.</p><div class="add-to-cart">Add to cart</div></article>

  <article class="product-card"><div class="product-image tone-white" role="img" aria-label="White N95 respirator with its box"><span></span></div><div class="product-head"><h3 class="product-name">N95 Mask</h3><span class="product-price">$28.00</span></div><p class="product-desc">Lorem ipsum dolor sit amet, consectetur elit. Morbi pellentesque, nisi ac tincidunt varius, erat nulla tempor est, ac malesuada ex quam sit amet ipsum.</p><div class="add-to-cart">Add to cart</div></article>
  <article class="product-card"><div class="product-image tone-teal" role="img" aria-label="Teal box of N95 protective masks"><span></span></div><div class="product-head"><h3 class="product-name">N95 Mask</h3><span class="product-price">$38.00</span></div><p class="product-desc">Lorem ipsum dolor sit amet, consectetur elit. Morbi pellentesque, nisi ac tincidunt varius, erat nulla tempor est, ac malesuada ex quam sit amet ipsum.</p><div class="add-to-cart">Add to cart</div></article>
  <article class="product-card"><div class="product-image tone-navy" role="img" aria-label="Box of disposable surgical face masks"><span></span></div><div class="product-head"><h3 class="product-name">Disposable Mask</h3><span class="product-price">$18.00</span></div><p class="product-desc">Lorem ipsum dolor sit amet, consectetur elit. Morbi pellentesque, nisi ac tincidunt varius, erat nulla tempor est, ac malesuada ex quam sit amet ipsum.</p><div class="add-to-cart">Add to cart</div></article>

  <article class="product-card"><div class="product-image tone-blue" role="img" aria-label="Box of 3-ply disposable face masks"><span></span></div><div class="product-head"><h3 class="product-name">Disposable Mask</h3><span class="product-price">$16.00</span></div><p class="product-desc">Lorem ipsum dolor sit amet, consectetur elit. Morbi pellentesque, nisi ac tincidunt varius, erat nulla tempor est, ac malesuada ex quam sit amet ipsum.</p><div class="add-to-cart">Add to cart</div></article>
  <article class="product-card"><div class="product-image tone-sky" role="img" aria-label="Box of surgical earloop masks"><span></span></div><div class="product-head"><h3 class="product-name">Surgical Mask</h3><span class="product-price">$22.00</span></div><p class="product-desc">Lorem ipsum dolor sit amet, consectetur elit. Morbi pellentesque, nisi ac tincidunt varius, erat nulla tempor est, ac malesuada ex quam sit amet ipsum.</p><div class="add-to-cart">Add to cart</div></article>
  <article class="product-card"><div class="product-image tone-dark" role="img" aria-label="Black reusable mask with its box"><span></span></div><div class="product-head"><h3 class="product-name">Reusable Mask</h3><span class="product-price">$26.00</span></div><p class="product-desc">Lorem ipsum dolor sit amet, consectetur elit. Morbi pellentesque, nisi ac tincidunt varius, erat nulla tempor est, ac malesuada ex quam sit amet ipsum.</p><div class="add-to-cart">Add to cart</div></article>

  <article class="product-card"><div class="product-image tone-white" role="img" aria-label="White N95 respirator with its box"><span></span></div><div class="product-head"><h3 class="product-name">N95 Mask</h3><span class="product-price">$28.00</span></div><p class="product-desc">Lorem ipsum dolor sit amet, consectetur elit. Morbi pellentesque, nisi ac tincidunt varius, erat nulla tempor est, ac malesuada ex quam sit amet ipsum.</p><div class="add-to-cart">Add to cart</div></article>
  <article class="product-card"><div class="product-image tone-teal" role="img" aria-label="Teal box of N95 protective masks"><span></span></div><div class="product-head"><h3 class="product-name">N95 Mask</h3><span class="product-price">$38.00</span></div><p class="product-desc">Lorem ipsum dolor sit amet, consectetur elit. Morbi pellentesque, nisi ac tincidunt varius, erat nulla tempor est, ac malesuada ex quam sit amet ipsum.</p><div class="add-to-cart">Add to cart</div></article>
  <article class="product-card"><div class="product-image tone-navy" role="img" aria-label="Box of disposable surgical face masks"><span></span></div><div class="product-head"><h3 class="product-name">Disposable Mask</h3><span class="product-price">$18.00</span></div><p class="product-desc">Lorem ipsum dolor sit amet, consectetur elit. Morbi pellentesque, nisi ac tincidunt varius, erat nulla tempor est, ac malesuada ex quam sit amet ipsum.</p><div class="add-to-cart">Add to cart</div></article>
</main>

<footer class="site-footer">
  <div class="logo"><span class="logo-dot"></span>curamed</div>
  <p class="footer-about">Lorem ipsum dolor sit amet, consectetur adipiscing elit. Morbi pellentesque, nisi ac tincidunt varius, erat nulla tempor est, ac malesuada ex quam sit amet ipsum.</p>

  <h4 class="footer-heading" style="left:556px">Navigation</h4>
  <ul class="footer-links" style="left:556px"><li>Home</li><li>Shop</li><li>About</li><li>Contact</li></ul>
  <ul class="footer-links" style="left:640px"><li>Privacy Policy</li><li>Returns &amp; Refunds</li><li>FAQs</li></ul>

  <h4 class="footer-heading" style="left:885px">Contact Us</h4>
  <div class="contact-item" style="top:70px">
    <svg width="16" height="22" viewBox="0 0 16 22" fill="none" stroke="#fff" stroke-width="1.3"><path d="M8 21S1 12 1 8a7 7 0 0114 0c0 4-7 13-7 13z"/><circle cx="8" cy="8" r="2.5"/></svg>
    <span>Address, City, Country<br>Exact address</span>
  </div>
  <div class="contact-item" style="top:127px">
    <svg width="18" height="18" viewBox="0 0 18 18" fill="none" stroke="#fff" stroke-width="1.3"><path d="M3 1l3 4-2 2c1 3 4 6 7 7l2-2 4 3-2 3C8 17 1 10 1 3z"/></svg>
    <span>+00 0 0000 00000</span>
  </div>
  <div class="contact-item" style="top:167px">
    <svg width="20" height="15" viewBox="0 0 20 15" fill="none" stroke="#fff" stroke-width="1.3"><rect x="1" y="1" width="18" height="13"/><path d="M1 1l9 7 9-7M1 14l7-6M19 14l-7-6"/></svg>
    <span>admin@curamed.com</span>
  </div>

  <div class="footer-bar">Curamed 2020 All Rights Reserved.</div>
</footer>

</body>
</html>
```